Bringing Radiant Artistry and Venturing Expressive Routines

FLYER FOR MENTAL SKILLS TRAINING AND CHOREOGRAPHY
For more information please see attachment.
For more information please see attachment
Thank you..

Target Market(s)

athletes, dancers and choreographers

Industry/Entity Type

Training

Font styles to use
Serif

Colors
32a5d7
0392cd
85cae6

Requirements
Must have
• email address: braverbymarisolquentin@postnest.example
• phone number: (555) 214-7730
• Facebook: www.fanpagehub.example/movementbymarisolquentin
Nice to have
• Everything that is in the file I have attached. Flattering and eye catching unisex color. Logo should be included on the very first page.

```html
<!DOCTYPE html>
<html lang="en">
<head>
<meta charset="utf-8">
<title>BRAVER – Mental Skills Training &amp; Choreography</title>
<link rel="stylesheet" href="https://fonts.googleapis.com/css2?family=Playfair+Display:wght@800&family=Arimo:ital,wght@0,400;0,700;1,700&family=Tinos:ital,wght@0,400;0,700;1,700&display=swap">
<style>
  :root {
    --teal: #1a96a6;
    --teal-dark: #127987;
    --aqua-light: #b3eef0;
    --cyan-figure: #1fe0e8;
    --ring: #8e92e4;
    --heading-teal: #25a5b5;
    --navy: #1d3f72;
    --ink: #111111;
    --paper: #ffffff;
  }
  * { margin: 0; padding: 0; box-sizing: border-box; }
  html, body { width: 927px; height: 1200px; overflow: hidden; background: var(--paper); }
  .flyer { position: relative; width: 927px; height: 1200px; overflow: hidden; background: var(--paper); color: var(--ink); }

  .ring { position: absolute; inset: 0; }

  .dancer-figure {
    position: absolute; left: 70px; top: 20px; width: 510px; height: 430px;
    background: radial-gradient(ellipse at 45% 50%, var(--cyan-figure) 0%, rgba(31,224,232,0.55) 45%, rgba(31,224,232,0) 72%);
  }

  .acronym { position: absolute; left: 512px; top: 70px; }
  .acronym-row { display: flex; align-items: center; height: 74px; }
  .acronym-letter {
    width: 70px; text-align: center;
    font-family: "Playfair Display", serif; font-weight: 800; font-size: 104px; line-height: 1;
  }
  .acronym-word { font-family: "Arimo", sans-serif; font-weight: 700; font-size: 33px; padding-left: 6px; margin-top: 18px; }
  .acronym-amp { position: absolute; left: 582px; top: 276px; font-family: "Arimo", sans-serif; font-weight: 700; font-size: 28px; }

  .founder { position: absolute; left: 166px; top: 452px; width: 320px; text-align: center; font-family: "Tinos", serif; font-size: 10.5px; line-height: 13px; }
  .founder-name { font-family: "Arimo", sans-serif; font-weight: 700; font-size: 14px; line-height: 17px; }
  .founder-role { font-family: "Arimo", sans-serif; font-weight: 700; font-style: italic; font-size: 14px; line-height: 17px; text-decoration: underline; margin-bottom: 1px; }

  .band { position: absolute; }
  .offer-band-shadow { left: -20px; top: 628px; width: 478px; height: 62px; background: var(--teal-dark); transform: rotate(-2.5deg); }
  .offer-band { left: -20px; top: 616px; width: 478px; height: 56px; background: var(--teal); transform: rotate(-2.5deg);
    display: flex; align-items: center; justify-content: center; }
  .offer-band h2 { font-family: "Tinos", serif; font-style: italic; font-weight: 700; font-size: 23px; color: var(--paper); padding-left: 24px; }

  .benefit-band-shadow { left: 506px; top: 570px; width: 460px; height: 92px; background: var(--teal); transform: rotate(-5deg); }
  .benefit-band { left: 516px; top: 552px; width: 440px; height: 86px; background: var(--aqua-light); transform: rotate(-5deg);
    display: flex; align-items: center; justify-content: center; }
  .benefit-band h2 { font-family: "Tinos", serif; font-style: italic; font-weight: 700; font-size: 22px; color: var(--navy); text-align: center; line-height: 1.3; padding-right: 20px; }

  .offer-box { position: absolute; left: 91px; top: 682px; width: 334px; height: 424px; background: var(--aqua-light); text-align: center; }
  .services { list-style: none; margin-top: 22px; font-family: "Tinos", serif; font-weight: 700; font-size: 16.5px; line-height: 22px; }
  .great-for { margin-top: 22px; font-family: "Arimo", sans-serif; font-weight: 700; font-size: 28px; line-height: 39px; color: var(--heading-teal); }
  .call { margin-top: 20px; font-family: "Arimo", sans-serif; font-weight: 700; font-size: 23px; line-height: 32px; }
  .phone { font-family: "Arimo", sans-serif; font-weight: 700; font-size: 24px; line-height: 32px; }

  .benefit-box { position: absolute; left: 522px; top: 648px; width: 405px; height: 238px; background: var(--aqua-light); }
  .benefit-list { width: 272px; margin: 58px 0 0 40px; font-family: "Tinos", serif; font-size: 13.5px; line-height: 17px; }
  .benefit-list li { margin-bottom: 1px; }

  .prices { position: absolute; left: 494px; top: 904px; font-family: "Tinos", serif; font-size: 15px; }
  .prices h3 { font-weight: 700; font-style: italic; font-size: 14.5px; line-height: 20px; text-decoration: underline; }
  .prices table { border-collapse: collapse; }
  .prices td { padding: 0; line-height: 21.5px; }
  .prices td:first-child { width: 160px; }

  .email { position: absolute; left: 474px; top: 1072px; font-family: "Tinos", serif; font-weight: 700; font-size: 16.5px; }

  .footer { position: absolute; left: 0; top: 1094px; width: 927px; height: 106px; }
  .footer-link { position: absolute; left: 0; top: 1120px; width: 927px; text-align: center; font-family: "Tinos", serif; font-weight: 700; font-size: 16px; color: var(--ink); }
</style>
</head>
<body>
<main class="flyer">
  <svg class="ring" width="927" height="1200" aria-hidden="true">
    <circle cx="452" cy="462" r="380" fill="none" stroke="var(--ring)" stroke-width="24" stroke-dasharray="5 10"/>
  </svg>

  <div class="dancer-figure" role="img" aria-label="Cyan silhouette of a leaping dancer"></div>

  <h1 class="acronym" aria-label="Bringing Radiant Artistry and Venturing Expressive Routines">
    <div class="acronym-row"><span class="acronym-letter">B</span><span class="acronym-word">ringing</span></div>
    <div class="acronym-row"><span class="acronym-letter">R</span><span class="acronym-word">adiant</span></div>
    <div class="acronym-row"><span class="acronym-letter">A</span><span class="acronym-word">rtistry</span></div>
    <div class="acronym-row"><span class="acronym-letter">V</span><span class="acronym-word">enturing</span></div>
    <div class="acronym-row"><span class="acronym-letter">E</span><span class="acronym-word">xpressive</span></div>
    <div class="acronym-row"><span class="acronym-letter">R</span><span class="acronym-word">outines</span></div>
  </h1>
  <span class="acronym-amp">&amp;</span>

  <section class="founder">
    <p class="founder-name">Marisol Quentin:</p>
    <p class="founder-role">The founder of BRAVER</p>
    <p>A former gymnast for Lakeshore State University</p>
    <p>A choreographer of gymnastic floor and beam routines</p>
    <p>A graduate of Lakeshore State University</p>
    <p>Bachelor of Arts in Liberal Arts and Sciences</p>
    <p>A graduate of Harlow University</p>
    <p>Masters in counseling with specialization in sport and health</p>
    <p>A member of Pulse Drive! A dance company founded in</p>
    <p>the Riverton-land area</p>
  </section>

  <div class="band benefit-band-shadow"></div>
  <div class="band benefit-band"><h2>Why Will You Benefit from<br>Mental Skills Training?</h2></div>

  <section class="benefit-box">
    <ol class="benefit-list">
      <li>Consider all athletic successes that you’ve had. What percentage of time were you mentally focused?</li>
      <li>Consider your athletic performance. What percentage of mistakes were considered to be mental errors?</li>
      <li>Consider your preparation. What percentage of time do you spend on mental training?</li>
    </ol>
  </section>

  <section class="offer-box">
    <ul class="services">
      <li>Mental Block Interventions</li>
      <li>Imagery Workshops</li>
      <li>Goal Setting Workshops</li>
      <li>Motivation Workshops</li>
      <li>Team Cohesion Activities</li>
      <li>Individual Sessions</li>
      <li>Choreography</li>
    </ul>
    <p class="great-for">Great For<br>Athletes • Dancers<br>Choreographers</p>
    <p class="call">Call today to sign up</p>
    <p class="phone">(555) 214-7730</p>
  </section>

  <div class="band offer-band-shadow"></div>
  <div class="band offer-band"><h2>What does BRAVER have to offer?</h2></div>

  <section class="prices">
    <h3>Package Prices</h3>
    <table>
      <tr><td>Team Workshops</td><td>$250 per contact/hour</td></tr>
      <tr><td>Coach Workshops</td><td>$250 per contact hour</td></tr>
      <tr><td>Individual Sessions</td><td>$100 per contact hour</td></tr>
      <tr><td>Floor Routines</td><td>$400 per gymnast</td></tr>
      <tr><td>Beam Routines</td><td>$150 per gymnast</td></tr>
      <tr><td>Dance Lessons</td><td>$25 per contact hour</td></tr>
    </table>
  </section>

  <p class="email">email: braverbymarisolquentin@postnest.example</p>
  <svg class="footer" width="927" height="106" aria-hidden="true">
    <polygon points="0,20 520,20 580,4 927,4 927,106 0,106" fill="var(--teal)"/>
    <polygon points="520,20 580,4 927,4 927,14 600,14 560,20" fill="var(--teal-dark)"/>
  </svg>
  <p class="footer-link">www.fanpagehub.example/movementbymarisolquentin</p>
</main>
</body>
</html>
```